Business Card Design

I am a GP with interest in Dermatology and Aesthetic Medicin, performing Botulinum Toxin Type A and Dermal Fillers treatmets in Cosmetic Dermatology clinic.

I am looking for a white colour, good quality white paper card may be of some special texture with black calligraphic writing but easy to read and not to wiggly- professional- looking.

Really appreciate your help.

Halyna

Cosmetic Dermatology Clinic

Dr Halyna Korbutiak, MBBS, MRCGP, DPD

Tel: 07841 615 092
halyna@medmailbox.org.uk

```html
<!DOCTYPE html>
<html lang="en">
<head>
<meta charset="utf-8">
<title>Cosmetic Dermatology Clinic — Business Card</title>
<link rel="stylesheet" href="https://fonts.googleapis.com/css2?family=Pompiere&display=swap">
<style>
  :root {
    --paper: #ffffff;
    --ink: #111111;
    --ornament-fill: #e6e6e6;
  }
  html, body {
    margin: 0;
    padding: 0;
    overflow: hidden;
    background: var(--paper);
  }
  .card {
    position: relative;
    width: 1200px;
    height: 791px;
    background: var(--paper);
    overflow: hidden;
  }
  .ornament-area {
    position: absolute;
    left: 404px;
    top: 282px;
    width: 796px;
    height: 48px;
    background: var(--ornament-fill);
  }
  .contact {
    position: absolute;
    right: 110px;
    top: 352px;
    margin: 0;
    text-align: right;
    font-family: "Pompiere", sans-serif;
    font-style: normal;
    font-size: 46px;
    line-height: 59px;
    letter-spacing: 2.5px;
    white-space: nowrap;
    color: var(--ink);
  }
  .contact span {
    display: block;
  }
</style>
</head>
<body>
  <div class="card">
    <div class="ornament-area" role="img" aria-label="Thin black wave line ornament running into a straight rule"></div>
    <address class="contact">
      <span class="clinic-name">Cosmetic Dermatology Clinic</span>
      <span class="doctor-name">Dr Halyna Korbutiak, MBBS, MRCGP, DPD</span>
      <span class="phone">Tel: 07841 615 092</span>
      <span class="email">halyna@medmailbox.org.uk</span>
    </address>
  </div>
</body>
</html>
```